Maple Hollow Ranch Business Card

Farm selling Nigerian Dwarf Goats, Bison, chickens, and miniature donkeys. Additionally we sell goats milk, goats milk soap and goat cheese, bison meat, bison heads, and bison skins, and chicken eggs.
Address 4127 Thornbury Lane
Briarwood, KY 42718
Phone number 615-382-9154
Website: MapleHollowRanch@ridgemail.net
I will upload my farm logo, cheese label, and soap label to give you ideas of my theme.
I want a really catchy card that people will remember.

```html
<!DOCTYPE html>
<html lang="en">
<head>
<meta charset="utf-8">
<title>Maple Hollow Ranch – Business Card</title>
<link rel="stylesheet" href="https://fonts.googleapis.com/css2?family=Cinzel:wght@400&family=Crimson+Text:wght@400;600&display=swap">
<style>
  :root {
    --backdrop: #cecac7;
    --card: #3a2f28;
    --card-edge: #2f2620;
    --gold: #e6a92b;
    --gold-light: #f3c85a;
    --gold-deep: #c9841a;
    --emblem: #5a4634;
    --emblem-ring: #8a5a2c;
  }
  * { box-sizing: border-box; margin: 0; padding: 0; }
  html, body {
    width: 1200px;
    height: 787px;
    overflow: hidden;
    background: var(--backdrop);
  }
  .stage {
    position: relative;
    width: 1200px;
    height: 787px;
  }
  .card {
    position: absolute;
    width: 485px;
    height: 295px;
    background: var(--card);
    overflow: hidden;
  }
  .card--front { left: 108px; top: 166px; }
  .card--back  { left: 612px; top: 333px; }

  .card__bands {
    position: absolute;
    left: 0;
    bottom: 0;
    width: 485px;
    height: 80px;
  }

  .brand {
    position: absolute;
    display: flex;
    flex-direction: column;
    align-items: center;
  }
  .brand__emblem {
    width: 118px;
    height: 118px;
    border-radius: 50%;
    background: radial-gradient(circle at 50% 45%, var(--emblem) 0%, var(--card-edge) 100%);
    border: 3px solid var(--emblem-ring);
  }
  .brand__name {
    margin-top: 8px;
    font-family: "Crimson Text", Georgia, serif;
    font-weight: 600;
    font-size: 20px;
    letter-spacing: 1px;
    color: var(--gold);
    white-space: nowrap;
  }
  .card--front .brand { left: 18px; top: 46px; width: 196px; }
  .card--back  .brand { left: 140px; top: 46px; width: 205px; }

  .contact {
    position: absolute;
    left: 244px;
    top: 74px;
    font-family: "Crimson Text", Georgia, serif;
    color: var(--gold);
  }
  .contact__name {
    font-family: "Cinzel", Georgia, serif;
    font-weight: 400;
    font-size: 25px;
    letter-spacing: 1px;
    color: var(--gold-light);
    margin-bottom: 14px;
    white-space: nowrap;
  }
  .contact__line {
    font-size: 14px;
    line-height: 20px;
    white-space: nowrap;
  }
  .contact__row {
    display: flex;
    align-items: center;
    gap: 6px;
    font-size: 14px;
    line-height: 24px;
    white-space: nowrap;
  }
  .contact__row--phone { margin-top: 6px; font-size: 16px; }
  .contact__icon { width: 13px; height: 13px; fill: var(--gold); }
</style>
</head>
<body>
<main class="stage">

  <section class="card card--front">
    <div class="brand">
      <div class="brand__emblem" role="img" aria-label="Farm emblem illustration area"></div>
      <div class="brand__name">Maple Hollow Ranch</div>
    </div>

    <div class="contact">
      <h1 class="contact__name">Dana Whitfield</h1>
      <p class="contact__line">Address 4127 Thornbury Lane</p>
      <p class="contact__line">Briarwood, KY 42718</p>
      <p class="contact__row contact__row--phone">
        <svg class="contact__icon" viewBox="0 0 16 16" aria-hidden="true"><path d="M2 5c0-2 2-3 3-3l1.5 3-1.5 1.5c.8 1.8 2.2 3.2 4 4L10.5 9l3 1.5c0 1-1 3-3 3C6 13.5 2 9.5 2 5z"/></svg>
        615-382-9154
      </p>
      <p class="contact__row">
        <svg class="contact__icon" viewBox="0 0 16 16" aria-hidden="true"><path d="M8 1.5 1 8h2v6.5h4v-4h2v4h4V8h2z"/></svg>
        MapleHollowRanch@ridgemail.net
      </p>
    </div>

    <svg class="card__bands" viewBox="0 0 485 80" aria-hidden="true">
      <defs>
        <linearGradient id="goldFront" x1="0" y1="0" x2="1" y2="0">
          <stop offset="0" stop-color="#c9841a"/>
          <stop offset=".5" stop-color="#f3c85a"/>
          <stop offset="1" stop-color="#e6a92b"/>
        </linearGradient>
      </defs>
      <path d="M0 20 Q240 -5 485 38 L485 48 Q240 8 0 32 Z" fill="url(#goldFront)"/>
      <path d="M0 44 Q240 20 485 56 L485 64 Q240 34 0 56 Z" fill="url(#goldFront)"/>
      <path d="M0 66 Q240 46 485 72 L485 80 L0 80 Z" fill="url(#goldFront)"/>
    </svg>
  </section>

  <section class="card card--back">
    <div class="brand">
      <div class="brand__emblem" role="img" aria-label="Farm emblem illustration area"></div>
      <div class="brand__name">Maple Hollow Ranch</div>
    </div>

    <svg class="card__bands" viewBox="0 0 485 80" aria-hidden="true">
      <defs>
        <linearGradient id="goldBack" x1="0" y1="0" x2="1" y2="0">
          <stop offset="0" stop-color="#c9841a"/>
          <stop offset=".5" stop-color="#f3c85a"/>
          <stop offset="1" stop-color="#e6a92b"/>
        </linearGradient>
      </defs>
      <path d="M0 20 Q240 -5 485 38 L485 48 Q240 8 0 32 Z" fill="url(#goldBack)"/>
      <path d="M0 44 Q240 20 485 56 L485 64 Q240 34 0 56 Z" fill="url(#goldBack)"/>
      <path d="M0 66 Q240 46 485 72 L485 80 L0 80 Z" fill="url(#goldBack)"/>
    </svg>
  </section>

</main>
</body>
</html>
```